Emmy award winning Hollywood sound studio needs a cool website

We need a website designed and coded to showcase our company and talent to our current and future clients. We are a post-production sound studio that works with Brambletoon, Vidora, Calder Sisters, Glimmerforge, and other major Hollywood studios and companies. We primarily work designing sound effects for animated TV shows like Puddlefin McGee, Rookie Rangers Roll!, Tiger Dojo: Lantern Riders, Fossil Valley Stampede Files, The Sly Crew, My Aunt the Starship Pilot, Spear of Helix, and the recent Vidora movie Wren and the Quiet. A website for our company would provide basic information about our studio and services, the kinds of projects we are currently working on and have worked on in the past, the awards we have won or been nominated for, and most importantly showcase our talented engineers so that producers and directors can get to know the people they might want to collaborate with. Our studio is located in Burbank, CA right in the heart of where all the studios are located. We have a basic company logo. We don't really have a color scheme to our studio so we're very open and flexible in that department. We have decorated our studio with a bit of an Art Deco style to invoke an old classy movie theater from the golden age of Hollywood. Our lobby resembles the lobby of a movie theater complete with a neon marquee where we post fun sayings or quotes from our shows. I think it would be fun for the website design to reflect that Art Deco/classic movie theater feeling. Another website that I think has a good simple design for inspiration is Fernhollow Audio: "www.fernaudio.example".
Target Market(s)
Major Hollywood Studios, Animation production companies, independent film/TV production
Industry/Entity Type
Hollywood, Television, Streaming, Entertainment, Games
Coding
Coded - Design and coding required
Number of Pages Required
5+ page
Look and feel

```html
<!DOCTYPE html>
<html lang="en">
<head>
<meta charset="utf-8">
<title>Echo Marquee — Audio Post Studio</title>
<link href="https://fonts.googleapis.com/css2?family=Poppins:wght@400;500;600;700;800&family=Righteous&display=swap" rel="stylesheet">
<style>
:root{
  --ink:#141414;
  --text:#3a3a3a;
  --muted:#6b6b6b;
  --line:#d9d9d9;
  --dark:#0f0f10;
  --btn:#2a2a2a;
  --navy:#2d3aa8;
  --sky:#159fdc;
  --sky-deep:#0d86c4;
  --band:#c9c9c9;
  --paper:#ffffff;
}
*{margin:0;padding:0;box-sizing:border-box}
html,body{width:1200px;height:5352px;overflow:hidden;background:var(--paper)}
body{font-family:"Poppins",sans-serif;color:var(--text);position:relative}
.page{position:relative;width:1200px;height:5352px}
.abs{position:absolute}
.btn{position:absolute;display:flex;align-items:center;justify-content:center;background:var(--btn);color:#fff;font-size:12px;font-weight:600;border-radius:24px;height:42px}
.band{position:absolute;left:0;width:1200px;height:28px;background:repeating-linear-gradient(90deg,var(--band) 0 2px,transparent 2px 8px);opacity:.75}

/* header */
.topbar{top:10px;right:125px;font-size:13px;font-weight:500;color:var(--ink);display:flex;gap:22px}
.topbar span{display:flex;align-items:center;gap:6px}
.brand{left:112px;top:30px;display:flex;align-items:center;gap:10px}
.brand-square{width:18px;height:18px;background:var(--ink)}
.brand-name{font-size:30px;font-weight:800;color:var(--ink);line-height:1;letter-spacing:1px}
.nav{top:64px;left:442px;display:flex;gap:34px;font-size:14px;font-weight:600;color:var(--ink)}

/* hero */
.hero{left:0;top:154px;width:1200px;height:525px;background:
  radial-gradient(ellipse 300px 240px at 73% 38%,rgba(150,160,175,.55),transparent 70%),
  radial-gradient(ellipse 520px 200px at 40% 95%,rgba(90,95,105,.55),transparent 75%),
  radial-gradient(circle at 72% 45%,#3e4249 0,#1f2126 40%,#0b0c0e 78%)}
.hero-title{left:112px;top:238px;font-family:"Righteous",sans-serif;color:#fff;line-height:1}
.hero-title .outline{font-size:80px;color:transparent;-webkit-text-stroke:2px #fff;display:block}
.hero-title .solid{font-size:88px;display:block;font-family:"Poppins",sans-serif;font-weight:800}
.hero-copy{left:112px;top:434px;width:430px;font-size:13px;color:#fff;line-height:24px}

h2.section-title{position:absolute;left:0;width:1200px;text-align:center;font-size:44px;font-weight:800;color:var(--ink);line-height:1}
.eyebrow{position:absolute;left:0;width:1200px;text-align:center;font-size:13px;color:var(--muted);letter-spacing:1px}
.studio-copy{left:245px;width:710px;text-align:center;font-size:15px;line-height:26px;color:var(--text)}

/* poster cards */
.poster{position:absolute;width:222px;height:260px;background:#fff;border-radius:6px;box-shadow:0 4px 18px rgba(0,0,0,.16);padding:14px}
.poster .art{width:100%;height:100%;border-radius:3px}
.caption{position:absolute;width:222px;text-align:center;font-size:11px;line-height:15px;color:var(--ink)}
.caption b{font-weight:700;font-size:11.5px;display:block}
.arrow{position:absolute;width:30px;height:30px;border-radius:50%;background:var(--ink);display:flex;align-items:center;justify-content:center}

/* services */
.service{position:absolute;width:299px;height:488px;background:#fff;box-shadow:0 4px 22px rgba(0,0,0,.13);border-radius:4px;padding:14px;text-align:center}
.service .art{height:216px;border-radius:3px}
.service .icon{width:74px;height:74px;border-radius:50%;background:var(--navy);border:5px solid #fff;margin:-38px auto 0;display:flex;align-items:center;justify-content:center;position:relative}
.service h3{font-size:15px;font-weight:600;color:var(--navy);margin-top:18px}
.service p{font-size:14px;line-height:25px;margin-top:12px;color:var(--text)}
.service .btn{position:static;width:148px;margin:16px auto 0}

/* team */
.member{position:absolute;width:230px;height:302px;background:#fff;box-shadow:0 4px 18px rgba(0,0,0,.14);border-radius:4px;padding:8px;text-align:center}
.member .art{height:193px}
.member h4{font-size:15px;font-weight:600;color:var(--ink);margin-top:22px;letter-spacing:.5px}
.member p{font-size:12px;line-height:16px;color:var(--text);margin-top:6px}

/* awards */
.award-row{position:absolute;left:465px;width:620px;height:44px;border-bottom:1px solid var(--line);font-size:16px;font-weight:500;color:var(--ink)}
.award-row span{position:absolute;top:0}

/* contact */
.contact-card{left:596px;top:4546px;width:498px;height:447px;background:var(--sky);z-index:2}
.contact-card h3{position:absolute;top:26px;left:0;width:100%;text-align:center;font-size:38px;font-weight:700;color:#fff}
.field{position:absolute;border:1.5px solid #fff;color:#fff;font-size:12px;font-weight:600;padding:8px 12px}
.footer{left:0;top:4912px;width:1200px;height:440px;background:var(--dark);color:#fff}
.footer .divider{position:absolute;top:120px;width:1px;height:150px;background:#444}
.social{display:inline-block;width:14px;height:14px;border-radius:50%;background:var(--sky);margin-right:10px}
</style>
</head>
<body>
<div class="page">

<!-- header -->
<div class="abs topbar">
  <span><svg width="12" height="12" viewBox="0 0 24 24"><path fill="#141414" d="M6.6 10.8a15 15 0 006.6 6.6l2.2-2.2c.3-.3.7-.4 1-.2 1.1.4 2.3.6 3.6.6.6 0 1 .4 1 1V20c0 .6-.4 1-1 1A17 17 0 013 4c0-.6.4-1 1-1h3.5c.6 0 1 .4 1 1 0 1.3.2 2.5.6 3.6.1.3 0 .7-.2 1z"/></svg>747-555-0182</span>
  <span><svg width="12" height="12" viewBox="0 0 24 24"><path fill="#141414" d="M2 21l21-9L2 3v7l15 2-15 2z"/></svg>hello@echomarqueepost.example</span>
</div>
<div class="abs brand"><div class="brand-square"></div><div class="brand-name">ECHO<br>MARQUEE</div></div>
<nav class="abs nav"><span>HOME</span><span>PEOPLE</span><span>SERVICES</span><span>PROJECT</span><span>LATEST</span><span>CONTACT US</span></nav>
<div class="band" style="top:118px"></div>

<!-- hero -->
<section class="abs hero" role="img" aria-label="Mixing console with headphones floating above it"></section>
<h1 class="abs hero-title"><span class="outline">Audio</span><span class="solid">Mastering</span></h1>
<p class="abs hero-copy">Lorem Ipsum is simply dummy text of the printing and typesetting industry. Lorem Ipsum has been the industry's standard dummy</p>
<div class="btn" style="left:112px;top:518px;width:185px;background:#fff;color:#141414">Read More</div>

<!-- studio -->
<h2 class="section-title" style="top:730px">OUR STUDIO</h2>
<p class="abs studio-copy" style="top:788px">Lorem Ipsum is simply dummy text of the printing and typesetting industry. Lorem Ipsum has been the industry's standard dummy</p>
<p class="abs studio-copy" style="top:867px">text ever since the 1500s, when an unknown printer took a galley of type and scrambled it to make a type specimen book. It has survived not only five centuries, but also the leap into electronic typesetting, remaining essentially unchanged. It was popularised in the 1960s with the release of Letraset sheets containing</p>
<div class="btn" style="left:508px;top:1015px;width:184px">Read More</div>
<div class="band" style="top:1120px"></div>

<!-- latest projects -->
<h2 class="section-title" style="top:1195px;font-size:42px;font-weight:700">Latest Projects</h2>
<div class="arrow" style="left:55px;top:1392px"><svg width="10" height="10" viewBox="0 0 10 10"><path d="M7 1L3 5l4 4" stroke="#fff" stroke-width="1.6" fill="none"/></svg></div>
<div class="arrow" style="left:1098px;top:1392px"><svg width="10" height="10" viewBox="0 0 10 10"><path d="M3 1l4 4-4 4" stroke="#fff" stroke-width="1.6" fill="none"/></svg></div>
<div class="poster" style="left:102px;top:1273px"><div class="art" role="img" aria-label="Animated series poster with dinosaur" style="background:radial-gradient(ellipse at 35% 40%,#b48a5e 0,#7a5a3c 35%,transparent 70%),radial-gradient(ellipse at 70% 85%,#c04a2a 0,transparent 45%),linear-gradient(180deg,#6e7f86,#3a3b2c 60%,#1e2418)"></div></div>
<div class="poster" style="left:355px;top:1273px"><div class="art" role="img" aria-label="Animated caped hero series poster" style="background:radial-gradient(ellipse at 50% 30%,#6f88a8 0,transparent 55%),linear-gradient(180deg,#3a4e6c,#1a2436 55%,#0b0f18)"></div></div>
<div class="poster" style="left:606px;top:1273px"><div class="art" role="img" aria-label="Animated dinosaur series poster" style="background:radial-gradient(ellipse at 55% 40%,#9a6a32 0,#5a3e20 35%,transparent 65%),radial-gradient(ellipse at 70% 88%,#d08a2a 0,transparent 35%),linear-gradient(180deg,#2a2520,#100e0c)"></div></div>
<div class="poster" style="left:858px;top:1273px"><div class="art" role="img" aria-label="Animated holiday movie poster" style="background:radial-gradient(ellipse at 50% 20%,#f6d35a 0,transparent 40%),radial-gradient(ellipse at 50% 80%,#d6403c 0,transparent 50%),linear-gradient(180deg,#2ab0e4,#1e7cc4 55%,#3c9a5a)"></div></div>
<div class="caption" style="left:102px;top:1548px"><b>NIGHTBLOOM TALES</b>Lena Hartwell<br>Copperline Studios</div>
<div class="caption" style="left:355px;top:1548px"><b>NIGHTBLOOM TALES</b>Lena Hartwell<br>Copperline Studios</div>
<div class="caption" style="left:606px;top:1548px"><b>NIGHTBLOOM TALES</b>Lena Hartwell<br>Copperline Studios</div>
<div class="caption" style="left:858px;top:1548px"><b>NIGHTBLOOM TALES</b>Lena Hartwell<br>Copperline Studios</div>
<div class="band" style="top:1661px"></div>

<!-- services -->
<div class="eyebrow" style="top:1738px">ABOUT MAKING MUSIC</div>
<h2 class="section-title" style="top:1762px">OUR SERVICES FOR YOU</h2>
<div class="service" style="left:106px;top:1895px">
  <div class="art" role="img" aria-label="Engineer at a recording desk" style="background:radial-gradient(ellipse at 70% 25%,#e8eef4 0,#9aa3ad 30%,transparent 60%),radial-gradient(ellipse at 25% 60%,#3a3c40 0,transparent 55%),linear-gradient(180deg,#6b7078,#2a2c30 60%,#141518)"></div>
  <div class="icon"><svg width="26" height="26" viewBox="0 0 24 24" fill="none" stroke="#fff" stroke-width="1.6"><rect x="3" y="3" width="18" height="18" rx="3"/><path d="M10 16V8l6-1.5v8"/><circle cx="8.5" cy="16" r="1.5"/><circle cx="14.5" cy="14.5" r="1.5"/></svg></div>
  <h3>Re-recording Mixing</h3>
  <p>Make a type specimen book.<br>It has survived not only five<br>centuries, but also the leap</p>
  <div class="btn">Read More</div>
</div>
<div class="service" style="left:442px;top:1835px">
  <div class="art" role="img" aria-label="Close view of mixing console faders" style="background:radial-gradient(ellipse at 60% 35%,#c4c6ca 0,#7d8085 35%,transparent 70%),linear-gradient(170deg,#5a5c60,#2a2b2e 55%,#111214)"></div>
  <div class="icon"><svg width="26" height="26" viewBox="0 0 24 24" fill="none" stroke="#fff" stroke-width="1.6"><rect x="3" y="4" width="18" height="16" rx="2"/><path d="M3 8h18M7 12h10M7 16h6"/></svg></div>
  <h3>Sound Design &amp; Editorial</h3>
  <p>Make a type specimen book.<br>It has survived not only five<br>centuries, but also the leap</p>
  <div class="btn">Read More</div>
</div>
<div class="service" style="left:781px;top:1895px">
  <div class="art" role="img" aria-label="DJ controller on a wooden table" style="background:radial-gradient(ellipse at 50% 65%,#3a3c44 0,#24262c 40%,transparent 70%),linear-gradient(180deg,#8a6a4e,#6a4e38 45%,#3c2c22)"></div>
  <div class="icon"><svg width="26" height="26" viewBox="0 0 24 24" fill="none" stroke="#fff" stroke-width="1.6"><rect x="3" y="5" width="18" height="13" rx="2"/><path d="M8 21h8M12 18v3M10 9l-2 2.5L10 14M14 9l2 2.5-2 2.5"/></svg></div>
  <h3>Sound Design And Mix In La</h3>
  <p>Make a type specimen book.<br>It has survived not only five<br>centuries, but also the leap</p>
  <div class="btn">Read More</div>
</div>
<div class="btn" style="left:494px;top:2381px;width:185px">Read More</div>
<div class="band" style="top:2485px"></div>

<!-- our projects -->
<h2 class="section-title" style="top:2570px;font-size:42px;font-weight:700">Our Projects</h2>
<div class="poster" style="left:102px;top:2649px"><div class="art" role="img" aria-label="Animated superhero movie poster" style="background:radial-gradient(ellipse at 45% 65%,#4a8a6a 0,#2a5a4a 40%,transparent 75%),linear-gradient(180deg,#1a2a2a,#1e4440 50%,#0c1a1a)"></div></div>
<div class="poster" style="left:355px;top:2649px"><div class="art" role="img" aria-label="Animated martial arts series poster" style="background:radial-gradient(ellipse at 60% 55%,#e6e2da 0,transparent 28%),radial-gradient(ellipse at 35% 45%,#e89a4a 0,#b8642e 40%,transparent 75%),linear-gradient(180deg,#d4884a,#6a3a2a 70%,#2a1a1a)"></div></div>
<div class="poster" style="left:606px;top:2649px"><div class="art" role="img" aria-label="Reality series cast poster" style="background:radial-gradient(ellipse at 50% 70%,#d8c0aa 0,transparent 55%),linear-gradient(180deg,#c8d8e6,#b8c6d2 40%,#a89888 80%,#6a5a4e)"></div></div>
<div class="poster" style="left:858px;top:2649px"><div class="art" role="img" aria-label="Animated adventure series poster" style="background:radial-gradient(ellipse at 50% 25%,#f06a8a 0,transparent 40%),radial-gradient(ellipse at 40% 75%,#6a4a3a 0,transparent 40%),linear-gradient(160deg,#9a3ad0,#5a3ad6 50%,#2a8ae0)"></div></div>
<div class="caption" style="left:102px;top:2926px"><b>NIGHTBLOOM TALES</b>Lena Hartwell<br>Copperline Studios</div>
<div class="caption" style="left:355px;top:2926px"><b>NIGHTBLOOM TALES</b>Lena Hartwell<br>Copperline Studios</div>
<div class="caption" style="left:606px;top:2926px"><b>NIGHTBLOOM TALES</b>Lena Hartwell<br>Copperline Studios</div>
<div class="caption" style="left:858px;top:2926px"><b>NIGHTBLOOM TALES</b>Lena Hartwell<br>Copperline Studios</div>
<div class="poster" style="left:102px;top:3023px"><div class="art" role="img" aria-label="Animated dog adventure movie poster" style="background:radial-gradient(ellipse at 50% 30%,#e2382a 0,transparent 45%),radial-gradient(ellipse at 50% 78%,#a8683a 0,transparent 45%),linear-gradient(180deg,#f6d45a,#f2b43a 60%,#e08a2a)"></div></div>
<div class="poster" style="left:355px;top:3023px"><div class="art" role="img" aria-label="Space drama movie poster" style="background:radial-gradient(ellipse at 50% 60%,#a86ae0 0,#5a2aa0 40%,transparent 75%),linear-gradient(180deg,#2a1a4a,#3a2070 50%,#120c22)"></div></div>
<div class="poster" style="left:606px;top:3023px"><div class="art" role="img" aria-label="Animated group comedy poster" style="background:radial-gradient(ellipse at 50% 80%,#e0a03a 0,transparent 35%),radial-gradient(ellipse at 50% 45%,#5a6aa8 0,transparent 60%),linear-gradient(180deg,#1c2a4c,#0e1426)"></div></div>
<div class="poster" style="left:858px;top:3023px"><div class="art" role="img" aria-label="Animated robot series poster" style="background:radial-gradient(ellipse at 55% 45%,#e0a070 0,transparent 40%),radial-gradient(ellipse at 30% 20%,#6a9ac8 0,transparent 40%),linear-gradient(180deg,#b86a3a,#5a3a3a 70%,#2a2a36)"></div></div>
<div class="caption" style="left:102px;top:3300px"><b>NIGHTBLOOM TALES</b>Lena Hartwell<br>Copperline Studios</div>
<div class="caption" style="left:355px;top:3300px"><b>NIGHTBLOOM TALES</b>Lena Hartwell<br>Copperline Studios</div>
<div class="caption" style="left:606px;top:3300px"><b>NIGHTBLOOM TALES</b>Lena Hartwell<br>Copperline Studios</div>
<div class="caption" style="left:858px;top:3300px"><b>NIGHTBLOOM TALES</b>Lena Hartwell<br>Copperline Studios</div>
<div class="btn" style="left:508px;top:3396px;width:184px">View All Projects</div>
<div class="band" style="top:3510px"></div>

<!-- team -->
<div class="eyebrow" style="top:3604px">THE WORLD OF MUSIC</div>
<h2 class="section-title" style="top:3632px;font-size:42px;font-weight:700">The Best Studio in the City</h2>
<div class="arrow" style="left:52px;top:3849px"><svg width="10" height="10" viewBox="0 0 10 10"><path d="M7 1L3 5l4 4" stroke="#fff" stroke-width="1.6" fill="none"/></svg></div>
<div class="arrow" style="left:1095px;top:3849px"><svg width="10" height="10" viewBox="0 0 10 10"><path d="M3 1l4 4-4 4" stroke="#fff" stroke-width="1.6" fill="none"/></svg></div>
<div class="member" style="left:100px;top:3714px"><div class="art" role="img" aria-label="Portrait of a studio engineer on a yellow backdrop" style="background:radial-gradient(ellipse 70px 110px at 50% 75%,#c9d2dc 0,#8a9aac 60%,transparent 100%),linear-gradient(180deg,#f0b440,#e39a2c)"></div><h4>JOHN SMITH</h4><p>Senior Vice President and<br>General Manager</p></div>
<div class="member" style="left:349px;top:3714px"><div class="art" role="img" aria-label="Portrait of a studio engineer by a brick wall" style="background:radial-gradient(ellipse 70px 110px at 50% 75%,#3a2a2e 0,#22181a 60%,transparent 100%),repeating-linear-gradient(180deg,#6e4434 0 10px,#5a3428 10px 12px)"></div><h4>JOHN SMITH</h4><p>Senior Vice President and<br>General Manager</p></div>
<div class="member" style="left:597px;top:3714px"><div class="art" role="img" aria-label="Portrait of a studio engineer on an orange backdrop" style="background:radial-gradient(ellipse 75px 110px at 50% 78%,#b4643a 0,#8a4a2a 60%,transparent 100%),linear-gradient(180deg,#f6b054,#ee9a3a)"></div><h4>JOHN SMITH</h4><p>Senior Vice President and<br>General Manager</p></div>
<div class="member" style="left:846px;top:3714px"><div class="art" role="img" aria-label="Portrait of a studio engineer on a grey backdrop" style="background:radial-gradient(ellipse 70px 110px at 50% 78%,#2a2c2e 0,#1a1b1c 60%,transparent 100%),linear-gradient(180deg,#7a7e82,#4a4e52)"></div><h4>JOHN SMITH</h4><p>Senior Vice President and<br>General Manager</p></div>

<!-- awards -->
<div class="abs" style="left:104px;top:4114px;font-size:13px;color:var(--muted);letter-spacing:1px">HUGE HONOR</div>
<div class="abs" style="left:104px;top:4130px;font-size:34px;font-weight:700;color:var(--ink)">Our Awards</div>
<p class="abs" style="left:464px;top:4114px;width:620px;font-size:14px;line-height:25px;color:var(--text)">Euismod in pellentesque massa placerat duis ultricies. Tristique nulla aliquet enim tortor at auctor urna nunc. Vel risusmodo viverra maecenas accumsan lacus vel facilisis volutpat. Leo urna molestie at elementum. Neque ornare aenean.</p>
<div class="award-row" style="top:4229px"><span style="left:0">Arno Valley Music Awards</span><span style="left:330px">Winner</span><span style="left:551px">2021</span></div>
<div class="award-row" style="top:4296px"><span style="left:0">Open Chorus Festival Awards</span><span style="left:330px">Silver Award</span><span style="left:551px">2020</span></div>
<div class="award-row" style="top:4364px"><span style="left:0">Free Stage Music Awards</span><span style="left:330px">Semi-Finalist</span><span style="left:551px">2019</span></div>
<div class="award-row" style="top:4431px;border-bottom:none"><span style="left:0">Harbor City Remix Fest</span><span style="left:330px">Silver Award</span><span style="left:551px">2019</span></div>

<!-- contact -->
<div class="abs" style="left:104px;top:4600px;width:400px;font-size:26px;font-weight:600;color:var(--ink);line-height:30px">Lorem Ipsum is simply<br>dummy text of the printing</div>
<p class="abs" style="left:104px;top:4680px;width:430px;font-size:14px;line-height:26px;color:var(--text)">Lorem Ipsum is simply dummy text of the printing and typesetting industry. Lorem Ipsum has been the industry's standard dummy text ever since the 1500s, when an unknown printer took a galley of type and scrambled it to make a type specimen book.</p>

<footer class="abs footer">
  <div class="abs" style="left:104px;top:140px;font-size:33px;font-weight:600;line-height:40px">We create &amp; process<br>musical pieces</div>
  <div class="divider" style="left:506px"></div>
  <div class="divider" style="left:837px"></div>
  <div class="abs" style="left:608px;top:138px;font-size:14px;font-weight:600">Address</div>
  <div class="abs" style="left:608px;top:180px;font-size:13px;line-height:22px">418 Lantern Row,<br>Burbank, California 91500,<br>United States</div>
  <div class="abs" style="left:903px;top:138px;font-size:14px;font-weight:600">Say Hello</div>
  <div class="abs" style="left:903px;top:180px;font-size:12px">hello@echomarqueepost.example</div>
  <div class="abs" style="left:903px;top:202px;font-size:22px;font-weight:600;color:var(--sky)">747-555-0182</div>
  <div class="abs" style="left:903px;top:248px"><span class="social"></span><span class="social"></span><span class="social"></span></div>
  <div class="abs" style="left:104px;top:320px;width:992px;height:1px;background:#333"></div>
  <div class="abs" style="left:104px;top:382px;font-size:11px;color:#cfcfcf;letter-spacing:.5px">HOME &nbsp;| &nbsp;&nbsp;PEOPLE &nbsp;| &nbsp;&nbsp;SERVICES &nbsp;| &nbsp;&nbsp;PROJECT &nbsp;| &nbsp;&nbsp;LATEST &nbsp;| &nbsp;&nbsp;CONTACT US</div>
  <div class="abs" style="left:752px;top:382px;font-size:11px;color:#cfcfcf">ECHO MARQUEE © 2024. ALL RIGHTS RESERVED.</div>
  <div class="abs" style="left:1058px;top:374px;width:28px;height:28px;border-radius:50%;background:var(--sky);display:flex;align-items:center;justify-content:center"><svg width="10" height="10" viewBox="0 0 10 10"><path d="M1 7l4-4 4 4" stroke="#fff" stroke-width="1.6" fill="none"/></svg></div>
</footer>

<div class="abs contact-card">
  <h3>Get in touch</h3>
  <div class="field" style="left:37px;top:119px;width:210px;height:48px">Name:</div>
  <div class="field" style="left:261px;top:119px;width:208px;height:48px">Phone:</div>
  <div class="field" style="left:37px;top:191px;width:210px;height:48px">Email:</div>
  <div class="field" style="left:261px;top:191px;width:208px;height:48px">Address:</div>
  <div class="field" style="left:37px;top:266px;width:432px;height:96px">Comments:</div>
  <div class="btn" style="left:168px;top:380px;width:185px;background:var(--sky-deep);color:#fff;border:1px solid #0b6fa3">Submit Now</div>
</div>

</div>
</body>
</html>
```